PawHush business card

Looking for a fun and cool biz card for a new company with patent pending products. I have products to help and protect dogs hearing. My colors are pantone blue and orange.
Updates

Please add tag line: Protect the ones you love...even your PawHushes!

Target Market(s)

Animal/Dog lovers!

Industry/Entity Type

Retail

Contact Information for Business Card

I'm looking for something simple yet fun with all the info included for biz cards

Colors
0555a3
f78f20

Requirements
Must have
• Logo
Nice to have
• name, website and email
Should not have
• phone number

```html
<!DOCTYPE html>
<html lang="en">
<head>
<meta charset="utf-8">
<title>PawHush business card</title>
<link rel="stylesheet" href="https://fonts.googleapis.com/css2?family=Montserrat:wght@500;600;700&display=swap">
<style>
  :root {
    --backdrop: #2b2b2b;
    --paper: #f2f2f2;
    --brand-blue: #0a2f8a;
    --brand-orange: #fc5000;
    --ink-white: #ffffff;
  }
  html, body {
    margin: 0;
    padding: 0;
    width: 1200px;
    height: 960px;
    overflow: hidden;
    background: var(--backdrop);
    font-family: "Montserrat", Arial, sans-serif;
  }
  .stage { position: relative; width: 1200px; height: 960px; }
  .card {
    position: absolute;
    left: 300px;
    width: 600px;
    height: 342px;
    overflow: hidden;
    box-shadow: 0 3px 8px rgba(0,0,0,.45);
  }
  .card--front { top: 127px; background: var(--paper); }
  .card--back { top: 510px; background: var(--brand-orange); }

  .front-panel { position: absolute; inset: 0; }

  .wordmark {
    position: absolute;
    margin: 0;
    font-weight: 700;
    letter-spacing: -0.5px;
    line-height: 1;
  }
  .card--front .wordmark {
    left: 33px;
    top: 139px;
    font-size: 56px;
    color: var(--brand-orange);
  }
  .card--back .wordmark {
    left: 0;
    right: 0;
    top: 122px;
    text-align: center;
    font-size: 74px;
    color: var(--brand-blue);
  }

  .contact {
    position: absolute;
    right: 40px;
    top: 95px;
    text-align: right;
    color: var(--ink-white);
  }
  .contact__name {
    margin: 0;
    font-size: 19px;
    font-weight: 700;
    color: var(--brand-orange);
    letter-spacing: 0.3px;
  }
  .contact__role {
    margin: 2px 0 0;
    font-size: 15px;
    font-weight: 700;
    letter-spacing: 0.5px;
  }
  .contact__address {
    margin: 20px 0 0;
    font-style: normal;
    font-size: 14px;
    font-weight: 500;
    line-height: 18px;
  }
  .contact__lines { margin: 17px 0 0; padding: 0; list-style: none; font-size: 14px; font-weight: 500; line-height: 21px; }
  .contact__lines li { display: flex; justify-content: flex-end; align-items: center; gap: 8px; }
  .contact__lines svg { width: 13px; height: 13px; flex: none; }

  .tagline {
    position: absolute;
    left: 0;
    right: 0;
    top: 285px;
    margin: 0;
    text-align: center;
    font-size: 13.5px;
    font-weight: 600;
    color: var(--brand-blue);
  }
</style>
</head>
<body>
<main class="stage">
  <section class="card card--front" aria-label="Business card front">
    <svg class="front-panel" viewBox="0 0 600 342" width="600" height="342" aria-hidden="true">
      <polygon points="370,28 378,0 374,0 285,342 305,342" fill="var(--brand-orange)"/>
      <polygon points="378,0 600,0 600,342 305,342" fill="var(--brand-blue)"/>
      <polygon points="376,0 380,0 307,342 302,342" fill="var(--ink-white)"/>
    </svg>
    <h1 class="wordmark">PawHush</h1>
    <div class="contact">
      <p class="contact__name">MARA LINDQVIST</p>
      <p class="contact__role">CEO/FOUNDER</p>
      <address class="contact__address">2140 Willow Bend Road<br>Fairbanks, Alaska 99701</address>
      <ul class="contact__lines">
        <li>mara@pawhush.com
          <svg viewBox="0 0 13 13" aria-hidden="true"><rect x="0.5" y="2.5" width="12" height="8.5" fill="var(--brand-orange)"/><polyline points="0.5,2.5 6.5,7.5 12.5,2.5" fill="none" stroke="var(--brand-blue)" stroke-width="1.2"/></svg>
        </li>
        <li>www.pawhush.com
          <svg viewBox="0 0 13 13" aria-hidden="true"><circle cx="6.5" cy="6.5" r="6" fill="var(--brand-orange)"/><ellipse cx="6.5" cy="6.5" rx="2.6" ry="6" fill="none" stroke="var(--brand-blue)" stroke-width="1"/><line x1="0.5" y1="6.5" x2="12.5" y2="6.5" stroke="var(--brand-blue)" stroke-width="1"/></svg>
        </li>
      </ul>
    </div>
  </section>

  <section class="card card--back" aria-label="Business card back">
    <p class="wordmark">PawHush</p>
    <p class="tagline">Protect the ones you love...even your PawHushes!</p>
  </section>
</main>
</body>
</html>
```